Invitation Design Project

I need a customized graphic design for my wedding invitation.I want it to be non-traditional wedding invite. The design in mind is like a movie poster graphics while adopting 'the bright days on the islands' font style and colors that create a light mood at the front page.Inside pages can be similar to movie posters with dark background similar to that of Grey harbor.Wedding related art/graphics can be integrated within the design.Wordings can be discussed later.

Industry/Entity Type

Graphic Design

Requirements
Must have
• Other must have features are our pictures as couple which will be sent .
Nice to have
• we would like to have the words

"our wedding.

more fun if you'll come!"

on the front cover.

```html
<!DOCTYPE html>
<html lang="en">
<head>
<meta charset="utf-8">
<title>Our Wedding – Invitation Cover</title>
<link rel="stylesheet" href="https://fonts.googleapis.com/css2?family=Nunito:wght@900&family=Ubuntu:wght@500&family=Roboto+Condensed:wght@700&display=swap">
<style>
  :root {
    --stage: #2a2e2a;
    --paper: #ffffff;
    --orange: #f26a1b;
    --orange-soft: #f8a25a;
    --tab-blue: #0f5fa8;
    --navy: #0b3f86;
    --ink-navy: #0d2a6b;
    --cyan: #17a6d6;
    --red-orange: #ec4a12;
    --frame-shadow: rgba(0, 0, 0, 0.35);
  }
  * { box-sizing: border-box; margin: 0; padding: 0; }
  html, body {
    width: 1200px;
    height: 848px;
    overflow: hidden;
    background: var(--stage);
  }
  .invitation-cover {
    position: absolute;
    left: 140px;
    top: 104px;
    width: 920px;
    height: 640px;
    display: flex;
    background: var(--paper);
    box-shadow: 0 10px 40px rgba(0, 0, 0, 0.5);
  }
  .glow-panel {
    width: 380px;
    height: 100%;
    background: radial-gradient(ellipse 170px 200px at 52% 45%, #ffffff 0%, #ffffff 25%, var(--orange-soft) 65%, var(--orange) 100%);
  }
  .front-panel {
    position: relative;
    flex: 1;
    height: 100%;
  }
  .title-tabs {
    position: absolute;
    top: 0;
    left: 0;
    width: 100%;
    display: flex;
    gap: 4px;
    padding: 0 0 0 4px;
  }
  .title-tab {
    position: relative;
    width: 50px;
    height: 74px;
  }
  .title-tab::before {
    content: "";
    position: absolute;
    left: 0;
    top: 0;
    width: 50px;
    height: 46px;
    background: var(--tab-blue);
    border-radius: 14px 14px 0 0;
  }
  .title-tab span {
    position: absolute;
    left: 2px;
    top: 26px;
    width: 46px;
    height: 46px;
    border-radius: 13px;
    background: var(--orange-soft);
    font-family: "Nunito", sans-serif;
    font-weight: 900;
    font-size: 34px;
    line-height: 46px;
    text-align: center;
    color: var(--paper);
  }
  .title-tab--our span { color: var(--tab-blue); }
  .couple-photo-frame {
    position: absolute;
    left: 0;
    top: 140px;
    width: 262px;
    height: 270px;
    padding: 10px 10px 10px 0;
    background: var(--paper);
    border-radius: 0 28px 28px 0;
    box-shadow: 10px 14px 18px var(--frame-shadow);
  }
  .couple-photo {
    width: 100%;
    height: 100%;
    border-radius: 0 20px 20px 0;
    background: linear-gradient(180deg, #dfe6e4 0%, #5d7f5a 28%, #9aa7a4 48%, #4d6258 75%, #3c4d43 100%);
  }
  .tagline {
    position: absolute;
    right: 36px;
    bottom: 22px;
    padding-left: 14px;
    border-left: 3px solid var(--orange);
  }
  .tagline-top {
    font-family: "Ubuntu", sans-serif;
    font-weight: 500;
    font-size: 54px;
    line-height: 1.05;
    color: var(--navy);
    letter-spacing: 1px;
  }
  .tagline-bottom {
    font-family: "Roboto Condensed", sans-serif;
    font-weight: 700;
    font-size: 56px;
    line-height: 1.1;
    letter-spacing: -1px;
  }
  .tagline-if { color: var(--ink-navy); }
  .tagline-you { color: var(--cyan); }
  .tagline-come { color: var(--red-orange); }
</style>
</head>
<body>
  <main class="invitation-cover">
    <div class="glow-panel"></div>
    <section class="front-panel">
      <h1 class="title-tabs" aria-label="Our Wedding">
        <span class="title-tab title-tab--our"><span>O</span></span>
        <span class="title-tab title-tab--our"><span>U</span></span>
        <span class="title-tab title-tab--our"><span>R</span></span>
        <span class="title-tab"><span>W</span></span>
        <span class="title-tab"><span>E</span></span>
        <span class="title-tab"><span>D</span></span>
        <span class="title-tab"><span>D</span></span>
        <span class="title-tab"><span>I</span></span>
        <span class="title-tab"><span>N</span></span>
        <span class="title-tab"><span>G</span></span>
      </h1>
      <div class="couple-photo-frame">
        <div class="couple-photo" role="img" aria-label="Photo of the couple standing in front of a waterfall"></div>
      </div>
      <p class="tagline">
        <span class="tagline-top">more fun</span><br>
        <span class="tagline-bottom"><span class="tagline-if">if</span> <span class="tagline-you">you’ll</span> <span class="tagline-come">come!</span></span>
      </p>
    </section>
  </main>
</body>
</html>
```